Webdesign für Steuerberaterin
Zielgruppe
Ich bin Steuerberaterin. Meine Zielgruppe sind sowohl Privatpersonen als auch Unternehmer sowie Männer und Frauen.
Aufgabenstellung
Bitte mein Logo und Foto mit berücksichtigen. Ich möchte keine Website, auf der alle 'Reiter' als eine Seite von oben nach unten durchlaufen. Sondern wirklich einzelne, voneinander getrennte Seiten.

```html
<!DOCTYPE html>
<html lang="de">
<head>
<meta charset="utf-8">
<title>Sabine Hortmann – Steuerberaterin</title>
<link rel="stylesheet" href="https://fonts.googleapis.com/css2?family=Crimson+Text&family=PT+Sans:wght@400;700&display=swap">
<style>
  :root {
    --sidebar: #1b191e;
    --gold: #a8822a;
    --gold-nav: #c1902c;
    --gold-band: #d9b53b;
    --gold-band-dark: #c9a22d;
    --text: #525252;
    --paper: #ffffff;
    --photo-light: #ececec;
    --photo-mid: #d9d9dc;
    --photo-dark: #2a2c38;
  }
  * { margin: 0; padding: 0; box-sizing: border-box; }
  html, body { width: 1200px; height: 960px; overflow: hidden; background: var(--paper); }
  .page { position: relative; width: 1200px; height: 960px; background: var(--paper); font-family: "PT Sans", sans-serif; }

  .sidebar { position: absolute; left: 0; top: 0; width: 243px; height: 934px; background: var(--sidebar); }

  .brand {
    position: absolute; left: 214px; top: 48px; width: 132px; height: 140px;
    background: var(--paper);
    display: flex; flex-direction: column; align-items: center; justify-content: center; gap: 10px;
  }
  .brand-square { width: 14px; height: 14px; background: var(--gold); }
  .brand-name {
    font-family: "Crimson Text", serif; font-size: 17px; color: var(--gold);
    text-align: center; line-height: 1.15;
  }

  .main-nav { position: absolute; left: 80px; top: 298px; list-style: none; }
  .main-nav li { height: 44px; }
  .main-nav a { font-size: 14px; color: var(--gold-nav); text-decoration: none; }

  .page-title {
    position: absolute; left: 429px; top: 172px; width: 596px;
    font-family: "Crimson Text", serif; font-weight: 400; font-size: 25px;
    color: var(--gold); text-align: center; margin-left: -22px;
  }
  .title-rule { position: absolute; left: 429px; top: 222px; width: 596px; height: 2px; background: var(--gold); }

  .portrait {
    position: absolute; left: 213px; top: 267px; width: 402px; height: 288px;
    background:
      radial-gradient(ellipse 32% 60% at 50% 100%, var(--photo-dark) 0%, var(--photo-dark) 55%, transparent 56%),
      linear-gradient(135deg, var(--photo-light), var(--photo-mid));
  }

  .welcome {
    position: absolute; left: 660px; top: 297px; width: 485px;
    text-align: center; color: var(--text); font-size: 15.5px; line-height: 21.7px;
  }
  .welcome h2 { font-size: 16px; font-weight: 700; margin-bottom: 23px; }
  .welcome p + p { margin-top: 22px; }

  .footer-band {
    position: absolute; left: 0; top: 934px; width: 1200px; height: 26px;
    background: linear-gradient(180deg, var(--gold-band), var(--gold-band-dark));
  }
</style>
</head>
<body>
<div class="page">
  <aside class="sidebar"></aside>

  <div class="brand">
    <span class="brand-square"></span>
    <span class="brand-name">Sabine Hortmann</span>
  </div>

  <ul class="main-nav">
    <li><a href="#">Über mich</a></li>
    <li><a href="#">Leistungen</a></li>
    <li><a href="#">Kontakt</a></li>
    <li><a href="#">Impressum</a></li>
  </ul>

  <h1 class="page-title">Schön, dass Sie da sind</h1>
  <div class="title-rule"></div>

  <div class="portrait" role="img" aria-label="Porträtfoto der Steuerberaterin im dunklen Blazer vor heller Steinwand"></div>

  <section class="welcome">
    <h2>Ich freue mich, dass Sie den Weg zu mir gefunden haben!</h2>
    <p>Sie sind bei mir genau richtig:<br>
    Egal, ob Sie Privatperson sind, die Ihre Einkommensteuer-Erklärung<br>
    in vertrauensvolle Hände geben möchte,<br>
    oder Unternehmer, der sich z.B. das „Rundum-Sorglos-Paket“<br>
    mit Buchführung, Jahresabschluss und Steuererklärungen wünscht.</p>
    <p>Schauen Sie sich hier gerne um und melden Sie sich bei mir<br>
    – ich bin bei jedem steuerlichen Thema<br>
    gerne Ihr kompetenter und zuverlässiger Ansprechpartner.</p>
    <p>Für mich ist es eine Selbstverständlichkeit,<br>
    dass ich auch nach mehr als 12 Jahren Berufserfahrung<br>
    durch permanente Fortbildungen immer auf dem aktuellsten Stand<br>
    der relevanten Gesetze und Verordnungen bin.<br>
    Nur so kann ich Sie bestmöglich beraten.</p>
  </section>

  <div class="footer-band"></div>
</div>
</body>
</html>
```